Business Card Design

I'm a young beekeeper (22 years old) just starting out. I own and run 80 hives and would like to eventually build up to 1000. My aim is to run it in tandem with our family farm that is currently running sheep and beef. Unlike a number of honey companies on the East Coast (or the North Island, NZ) I am local and will expand onto the lease blocks that our family is also leasing. I want a simple plain logo/photo. The designer may wish to use one of the photos as a background outline or however they chose. The mountain is Moekaha and our farm borders one side of it.

Target Market(s)

From local land owners to wholesale honey buyers

Industry/Entity Type

Farm

Contact Information for Business Card

Moekaha Honey
Manager Owner Rewene Tolland
email moekahahoney@pelvanmail.co.nz
mobile 0219473061

Requirements
Must have
• The details submitted. The brand Moekaha Honey to be the main feature. The other details can be smaller.
Should not have
• Must not include a picture of a bee or hive. Use a modern font. Don't use koru but may incorporate poutama.

```html
<!DOCTYPE html>
<html lang="en">
<head>
<meta charset="utf-8">
<title>Moekaha Honey — Business Card</title>
<link rel="stylesheet" href="https://fonts.googleapis.com/css2?family=Mulish:wght@400;700&display=swap">
<style>
  :root {
    --paper: #ffffff;
    --royal-blue: #0a24f5;
    --sky-blue: #74d9fb;
    --ink-white: #ffffff;
  }
  * { margin: 0; padding: 0; box-sizing: border-box; }
  html, body {
    width: 1200px;
    height: 703px;
    overflow: hidden;
    background: var(--paper);
  }
  .card {
    position: relative;
    width: 1200px;
    height: 703px;
    background: var(--paper);
    font-family: "Mulish", Arial, sans-serif;
    overflow: hidden;
  }
  .card__backdrop {
    position: absolute;
    inset: 0;
    width: 1200px;
    height: 703px;
  }
  .mountain { fill: var(--royal-blue); }
  .panel--royal { fill: var(--royal-blue); }
  .panel--sky { fill: var(--sky-blue); }

  .brand {
    position: absolute;
    left: 0;
    top: 196px;
    width: 800px;
    text-align: center;
    color: var(--ink-white);
    font-weight: 700;
    font-size: 92px;
    line-height: 1;
    letter-spacing: 2px;
  }
  .brand__sub {
    display: block;
    margin-top: 22px;
    font-size: 56px;
    letter-spacing: 24px;
  }

  .contact {
    position: absolute;
    left: 673px;
    top: 528px;
    color: var(--royal-blue);
  }
  .contact__name {
    font-weight: 400;
    font-size: 47px;
    line-height: 1;
    letter-spacing: 1px;
    text-transform: uppercase;
    margin-bottom: 26px;
  }
  .contact__line {
    display: flex;
    align-items: center;
    gap: 12px;
    font-size: 25px;
    line-height: 1;
    margin-bottom: 14px;
    margin-left: 3px;
  }
  .contact__icon { width: 26px; height: 26px; flex: none; }
  .contact__icon .disc { fill: var(--royal-blue); }
  .contact__icon .glyph { fill: none; stroke: var(--ink-white); stroke-width: 1.8; stroke-linejoin: round; }
</style>
</head>
<body>
<div class="card">
  <svg class="card__backdrop" viewBox="0 0 1200 703" xmlns="http://www.w3.org/2000/svg">
    <rect class="mountain" x="0" y="42" width="825" height="148" role="img" aria-label="Silhouette of Moekaha mountain ridge"/>
    <polygon class="panel--royal" points="0,189 825,189 476,703 0,703"/>
    <polygon class="panel--sky" points="825,189 1200,189 1200,703 476,703"/>
  </svg>

  <h1 class="brand">Moekaha<span class="brand__sub">HONEY</span></h1>

  <div class="contact">
    <p class="contact__name">Rewene Tolland</p>
    <p class="contact__line">
      <svg class="contact__icon" viewBox="0 0 26 26" aria-hidden="true">
        <circle class="disc" cx="13" cy="13" r="13"/>
        <rect class="glyph" x="9" y="6" width="8" height="14" rx="1.5"/>
      </svg>
      <span>0219473061</span>
    </p>
    <p class="contact__line">
      <svg class="contact__icon" viewBox="0 0 26 26" aria-hidden="true">
        <circle class="disc" cx="13" cy="13" r="13"/>
        <rect class="glyph" x="6.5" y="8.5" width="13" height="9"/>
        <polyline class="glyph" points="6.5,8.5 13,13.5 19.5,8.5"/>
      </svg>
      <span>moekahahoney@pelvanmail.co.nz</span>
    </p>
  </div>
</div>
</body>
</html>
```